DMR Property - Business Cards

Looking for a business card & general letterhead, signage etc design for our new logo.

Colours:
000a20
0056a2
00b5ef
0088ce
68cef2

Fonts:
Poppins
Karla

Please keep look and feel of new brand - example in the zip package I sent.

```html
<!DOCTYPE html>
<html lang="en">
<head>
<meta charset="utf-8">
<title>DMR Property – Business Cards</title>
<link href="https://fonts.googleapis.com/css2?family=Montserrat:wght@400;500;700&display=swap" rel="stylesheet">
<style>
  :root{
    --backdrop:#3b3b3d;
    --navy:#000a20;
    --card-back:#0f1429;
    --blue-deep:#0056a2;
    --blue-mid:#0088ce;
    --blue-bright:#00b5ef;
    --blue-soft:#68cef2;
    --ink:#1c1c1c;
    --paper:#ffffff;
  }
  *{margin:0;padding:0;box-sizing:border-box}
  html,body{width:1200px;height:689px;overflow:hidden;background:var(--backdrop)}
  body{position:relative;font-family:"Montserrat",sans-serif}
  .card{position:absolute;top:190px;width:540px;height:309px;border-radius:2px;box-shadow:0 18px 40px rgba(0,0,0,.45)}
  .card--back{left:30px;background:var(--card-back);display:flex;align-items:center;justify-content:center}
  .card--front{left:630px;background:var(--paper);overflow:hidden}
  .brand{font-weight:700;letter-spacing:.5px;white-space:nowrap}
  .card--back .brand{font-size:44px;color:#14306a}
  .card--front .brand{position:absolute;top:34px;right:34px;font-size:28px;color:var(--blue-deep)}
  .rule{position:absolute;height:1px;background:var(--ink)}
  .rule--top{left:34px;right:34px;top:100px}
  .person{position:absolute;left:34px;top:150px}
  .person__name{font-weight:700;font-size:21px;color:var(--blue-deep);letter-spacing:.3px}
  .person__role{font-weight:400;font-size:13px;color:var(--ink);letter-spacing:.5px;margin-top:3px}
  .rule--mid{left:34px;width:230px;top:208px}
  .contacts{position:absolute;left:34px;top:220px;list-style:none}
  .contacts li{display:flex;align-items:center;gap:9px;font-size:13px;color:var(--ink);height:24px}
  .contacts svg{width:14px;height:14px;flex:none}
  .address{position:absolute;right:34px;top:150px;text-align:right;font-size:13px;line-height:1.5;color:var(--ink);font-style:normal}
</style>
</head>
<body>
  <section class="card card--back" aria-label="Card back">
    <span class="brand">DMR Property</span>
  </section>

  <section class="card card--front" aria-label="Card front">
    <span class="brand">DMR Property</span>
    <div class="rule rule--top"></div>

    <div class="person">
      <p class="person__name">DANIEL REEVES</p>
      <p class="person__role">MANAGING DIRECTOR</p>
    </div>
    <div class="rule rule--mid"></div>

    <ul class="contacts">
      <li>
        <svg viewBox="0 0 16 16" aria-hidden="true"><circle cx="8" cy="8" r="7.5" fill="var(--blue-mid)"/><path d="M5 4.5c.6-.4 1.3 1.2 1.3 1.8 0 .6-.8.7-.5 1.4.4.9 1 1.5 1.8 1.9.6.3.8-.5 1.4-.5.6 0 2.2.7 1.8 1.3-.5.9-1.5 1.3-2.5.9C6.4 10.4 5.4 9.3 4.8 7.6c-.4-1.1-.5-2.4.2-3.1z" fill="#fff"/></svg>
        055-210 874 316
      </li>
      <li>
        <svg viewBox="0 0 16 16" aria-hidden="true"><rect x="1" y="3.5" width="14" height="9" fill="var(--blue-mid)"/><path d="M1 3.5l7 5 7-5" fill="none" stroke="#fff" stroke-width="1.2"/></svg>
        info@dmrproperty.com
      </li>
      <li>
        <svg viewBox="0 0 16 16" aria-hidden="true"><g fill="none" stroke="var(--blue-mid)" stroke-width="1.3"><circle cx="8" cy="8" r="6.5"/><ellipse cx="8" cy="8" rx="3" ry="6.5"/><path d="M1.5 8h13M2.5 5h11M2.5 11h11"/></g></svg>
        www.dmrproperty.com
      </li>
    </ul>

    <address class="address">
      18 Harbour View Road<br>
      30917, Northvale
    </address>
  </section>
</body>
</html>
```